Weather card for guests at Fenwick’s Beach House

I am looking to have a card designed for my guests who stay over. The card should show the weather for the next day (emoji's), quote of the day, Activities of the day. It's for a beach house so it should be coastal/Beachy themed. The weather should have a high and a low. (I will fill in each card). It should be front and back. It should be a fun project. Think modern farmhouse. The top of each card should say something like Another great Day at 7 Harbor
Updates

If you google "turn down Service letter" or "hotel weather card". It will provide examples

Target Market(s)

Our guests who visit our beach house

Font styles to use
Sans Serif

Colors
0054AA
0677BA
7BADD7
CADEEF
E8F1F8

Requirements
Must have
• weather options, quote of the day, activity for the day
Nice to have
• Sand, seashells, seagulls
Should not have
• Should not be too busy and not childish

```html
<!DOCTYPE html>
<html lang="en">
<head>
<meta charset="utf-8">
<title>7 Harbor – Guest Weather Card</title>
<link rel="stylesheet" href="https://fonts.googleapis.com/css2?family=Quicksand:wght@400;500;600&display=swap">
<style>
  :root {
    --backdrop: #cc9e82;
    --card: #ffffff;
    --navy: #1b5ca6;
    --ink: #0054aa;
    --sky: #0677ba;
    --mist: #cadeef;
    --sand: #ecd49c;
    --sand-soft: #f6ead0;
    --wave-deep: #2ea6e0;
    --wave-mid: #22b4ea;
    --wave-light: #4cc6f2;
  }
  * { box-sizing: border-box; margin: 0; padding: 0; }
  html, body { width: 848px; height: 1200px; overflow: hidden; }
  body {
    position: relative;
    background: var(--backdrop);
    font-family: "Quicksand", sans-serif;
    color: var(--navy);
  }
  .card {
    position: absolute;
    background: var(--card);
    overflow: hidden;
  }
  .card--front { left: 79px; top: 64px; width: 690px; height: 487px; }
  .card--back { left: 108px; top: 640px; width: 633px; height: 447px; }

  .sand-corner {
    position: absolute; left: 0; top: 0;
    width: 52%; height: 62%;
    background: radial-gradient(ellipse at 0 0, var(--sand) 0%, var(--sand) 35%, var(--sand-soft) 55%, rgba(255,255,255,0) 72%);
  }
  .shell-corner {
    position: absolute; right: 0; top: 0;
    width: 34%; height: 70%;
    background: radial-gradient(ellipse at 100% 0, var(--sand-soft) 0%, #f8eedc 40%, rgba(255,255,255,0) 70%);
  }

  .brand-box {
    position: absolute;
    border: 1.5px solid var(--navy);
    display: flex; align-items: center; justify-content: center;
    font-weight: 500; letter-spacing: 0.5px;
  }
  .tagline { position: absolute; left: 0; right: 0; text-align: center; font-weight: 400; }

  .card--front .brand-box { left: 259px; top: 43px; width: 171px; height: 44px; font-size: 30px; }
  .card--front .tagline { top: 96px; font-size: 19px; }

  .weather-options { position: absolute; left: 0; top: 155px; width: 100%; height: 100px; }
  .weather-option { position: absolute; width: 64px; margin-left: -32px; text-align: center; }
  .weather-option svg { width: 64px; height: 64px; display: block; }
  .checkbox { display: block; width: 15px; height: 15px; border: 1.5px solid var(--navy); margin: 22px auto 0; }

  .temperature { position: absolute; left: 34px; top: 293px; width: 622px; height: 30px; }
  .temperature__track { position: absolute; left: 400px; right: 0; top: 3px; height: 21px; background: var(--mist); border-radius: 11px; }
  .temperature__field { position: absolute; left: 90px; top: 1px; width: 409px; height: 26px; border: 1.5px solid var(--navy); border-radius: 13px; background: var(--card); }
  .temperature__label {
    position: absolute; left: 0; top: 0; width: 118px; height: 30px;
    background: var(--navy); color: #fff; border-radius: 15px;
    font-size: 15px; font-weight: 500; display: flex; align-items: center; justify-content: center;
  }
  .temperature__value { position: absolute; top: 4px; font-size: 15px; }
  .temperature__value--high { left: 136px; }
  .temperature__value--low { left: 305px; }

  .quote-heading {
    position: absolute; left: 0; right: 0; top: 349px;
    text-align: center; font-size: 15px; text-decoration: underline; text-underline-offset: 3px;
  }

  .sea { position: absolute; left: 0; bottom: 0; width: 100%; }
  .card--front .sea { height: 64px; }
  .card--back .sea { height: 61px; }
  .sea svg { width: 100%; height: 100%; display: block; }
  .footer-rule { position: absolute; left: 0; height: 1px; background: rgba(255,255,255,0.9); }
  .footer-mark { position: absolute; color: #fff; font-size: 7px; }
  .card--front .footer-rule { top: 477px; width: 630px; }
  .card--front .footer-mark { top: 472px; left: 636px; }
  .card--back .footer-rule { top: 437px; width: 576px; }
  .card--back .footer-mark { top: 432px; left: 585px; }

  .card--back .brand-box { left: 223px; top: 83px; width: 187px; height: 48px; font-size: 33px; }
  .card--back .tagline { top: 141px; font-size: 20px; }

  .activities {
    position: absolute; left: 25px; top: 234px; width: 583px; height: 121px;
    border: 1.2px solid var(--sky); border-radius: 26px;
  }
  .activities__title {
    position: absolute; left: 50%; top: -9px; transform: translateX(-50%);
    background: var(--card); padding: 0 13px; color: var(--sky);
    font-size: 13px; letter-spacing: 0.4px; white-space: nowrap; line-height: 16px;
  }
  .activities__line { position: absolute; left: 35px; right: 40px; border-top: 1px dotted var(--sky); }
</style>
</head>
<body>

<svg width="0" height="0" style="position:absolute" aria-hidden="true">
  <defs>
    <symbol id="cloud" viewBox="0 0 60 60">
      <path d="M15 46 a9 9 0 0 1 1-18 a12 12 0 0 1 22-5 a10 10 0 0 1 10 13 a5 5 0 0 1 -2 10 z" fill="#fff" stroke="#1b5ca6" stroke-width="2" stroke-linejoin="round"/>
    </symbol>
    <symbol id="rays" viewBox="0 0 60 60">
      <circle cx="30" cy="30" r="21" fill="none" stroke="#1b5ca6" stroke-width="6" stroke-dasharray="1.8 6.45"/>
      <circle cx="30" cy="30" r="18" fill="#fff"/>
      <circle cx="30" cy="30" r="13" fill="#fff" stroke="#1b5ca6" stroke-width="2"/>
    </symbol>
    <symbol id="waves" viewBox="0 0 690 64" preserveAspectRatio="none">
      <path d="M0 8 C40 -4 80 14 125 12 C170 10 190 -2 240 0 C290 2 310 14 350 12 C390 10 430 -2 480 0 C530 2 550 14 595 12 C635 10 660 0 690 4 V64 H0 Z" fill="#2ea6e0"/>
      <path d="M0 26 C60 16 110 34 180 30 C250 26 300 18 360 24 C420 30 470 36 540 28 C600 22 650 20 690 24 V64 H0 Z" fill="#22b4ea"/>
      <path d="M0 48 C80 40 160 46 260 44 C360 42 440 38 540 42 C610 45 660 44 690 42 V64 H0 Z" fill="#4cc6f2"/>
    </symbol>
  </defs>
</svg>

<section class="card card--front">
  <div class="sand-corner" role="img" aria-label="Sandy beach illustration with flying seagulls"></div>
  <div class="shell-corner" role="img" aria-label="Seashells and starfish scattered on sand"></div>

  <div class="brand-box">7 Harbor</div>
  <p class="tagline">Another Great Day</p>

  <div class="weather-options">
    <div class="weather-option" style="left:69px">
      <svg viewBox="0 0 60 60" aria-label="Sunny"><use href="#rays"/></svg>
      <span class="checkbox"></span>
    </div>
    <div class="weather-option" style="left:176px">
      <svg viewBox="0 0 60 60" aria-label="Partly cloudy">
        <use href="#rays" x="-10" y="-8" width="44" height="44"/>
        <use href="#cloud" x="4" y="4" width="56" height="56"/>
      </svg>
      <span class="checkbox"></span>
    </div>
    <div class="weather-option" style="left:292px">
      <svg viewBox="0 0 60 60" aria-label="Sun and showers">
        <use href="#rays" x="-8" y="-12" width="44" height="44"/>
        <use href="#cloud" x="4" y="-8" width="56" height="56"/>
        <g stroke="#1b5ca6" stroke-width="2" stroke-linecap="round">
          <line x1="22" y1="42" x2="22" y2="50"/><line x1="28" y1="44" x2="28" y2="56"/>
          <line x1="34" y1="42" x2="34" y2="52"/><line x1="40" y1="44" x2="40" y2="54"/>
          <line x1="46" y1="42" x2="46" y2="49"/>
        </g>
      </svg>
      <span class="checkbox"></span>
    </div>
    <div class="weather-option" style="left:402px">
      <svg viewBox="0 0 60 60" aria-label="Cloudy">
        <use href="#cloud" x="-2" y="-16" width="34" height="34"/>
        <use href="#cloud" x="4" y="2" width="56" height="56"/>
      </svg>
      <span class="checkbox"></span>
    </div>
    <div class="weather-option" style="left:509px">
      <svg viewBox="0 0 60 60" aria-label="Rain">
        <use href="#cloud" x="2" y="-10" width="58" height="58"/>
        <g stroke="#1b5ca6" stroke-width="2" stroke-linecap="round">
          <line x1="18" y1="40" x2="10" y2="52"/><line x1="25" y1="40" x2="18" y2="50"/>
          <line x1="31" y1="40" x2="24" y2="52"/><line x1="38" y1="41" x2="33" y2="48"/>
          <line x1="46" y1="38" x2="36" y2="53"/>
        </g>
      </svg>
      <span class="checkbox"></span>
    </div>
    <div class="weather-option" style="left:616px">
      <svg viewBox="0 0 60 60" aria-label="Thunderstorm">
        <use href="#cloud" x="2" y="-14" width="58" height="58"/>
        <path d="M20 34 L14 44 L22 42 L16 54 L30 40 L22 41 L26 34 Z" fill="#1b5ca6"/>
        <g stroke="#1b5ca6" stroke-width="2" stroke-linecap="round">
          <line x1="33" y1="38" x2="33" y2="52"/><line x1="38" y1="40" x2="38" y2="50"/>
          <line x1="43" y1="38" x2="43" y2="48"/>
        </g>
      </svg>
      <span class="checkbox"></span>
    </div>
  </div>

  <div class="temperature">
    <div class="temperature__track"></div>
    <div class="temperature__field"></div>
    <div class="temperature__label">Temperature</div>
    <span class="temperature__value temperature__value--high">Highest :</span>
    <span class="temperature__value temperature__value--low">Lowest :</span>
  </div>

  <p class="quote-heading">Quote of the day</p>

  <div class="sea"><svg viewBox="0 0 690 64" preserveAspectRatio="none" aria-hidden="true"><use href="#waves" width="690" height="64"/></svg></div>
  <div class="footer-rule"></div>
  <span class="footer-mark">7 Harbor</span>
</section>

<section class="card card--back">
  <div class="sand-corner" role="img" aria-label="Sandy beach illustration with flying seagulls"></div>
  <div class="shell-corner" role="img" aria-label="Seashells and starfish scattered on sand"></div>

  <div class="brand-box">7 Harbor</div>
  <p class="tagline">Another Great Day</p>

  <div class="activities">
    <span class="activities__title">Activities for the day</span>
    <div class="activities__line" style="top:37px"></div>
    <div class="activities__line" style="top:70px"></div>
    <div class="activities__line" style="top:102px"></div>
  </div>

  <div class="sea"><svg viewBox="0 0 690 64" preserveAspectRatio="none" aria-hidden="true"><use href="#waves" width="690" height="64"/></svg></div>
  <div class="footer-rule"></div>
  <span class="footer-mark">7 Harbor</span>
</section>

</body>
</html>
```